Business price tag design for Furniture Business

Hello,

I have developed a tag for a home furniture business and need 1 more creative template. Please see attachment. I need the template to be very appealing.

Requirements:

1.Tag dimensions needs to be about the same as attached tag.
2. Tag design needs to be suitable for a home furniture business.
3. Tag needs to have locations for the following: Item Title, Now Price, Was Price, Product Number.
4. "The black shape at the bottom of attached tag could be removed.

I have no requirements on colors, but something professional is needed, preferably white background to reduce print ink consumption.

Please see attachment for clarification.

Industry/Entity Type

Retail

Font styles to use
Serif
Sans Serif

Requirements
Must have
• Please see Project Description.
Nice to have

```html
<!DOCTYPE html>
<html lang="en">
<head>
<meta charset="utf-8">
<title>Allied Furniture Depot – Price Tag</title>
<link href="https://fonts.googleapis.com/css2?family=Arimo:wght@400&display=swap" rel="stylesheet">
<style>
  :root {
    --tag-green: #8cc63f;
    --tag-brown: #8a5a3b;
    --tag-paper: #ffffff;
  }
  html, body {
    margin: 0;
    padding: 0;
    overflow: hidden;
    background: var(--tag-paper);
  }
  .price-tag {
    position: relative;
    width: 1200px;
    height: 2308px;
    background: var(--tag-paper);
    font-family: "Arimo", Arial, sans-serif;
    overflow: hidden;
  }
  .tag-frame {
    position: absolute;
    inset: 0;
  }
  .tag-text {
    position: absolute;
    margin: 0;
    font-weight: 400;
    line-height: 1;
    white-space: nowrap;
  }
  .store-name {
    left: 512px;
    top: 118px;
    font-size: 90px;
    line-height: 128px;
    color: var(--tag-green);
  }
  .new-flag {
    left: 884px;
    top: 592px;
    font-size: 62px;
    color: var(--tag-green);
  }
  .field-label {
    color: var(--tag-green);
  }
  .item-title-label { left: 536px; top: 676px; font-size: 62px; }
  .item-title {
    left: 536px;
    top: 806px;
    font-size: 82px;
    line-height: 114px;
    color: var(--tag-brown);
  }
  .product-number-label { left: 534px; top: 1186px; font-size: 54px; }
  .product-number {
    left: 534px;
    top: 1268px;
    font-size: 62px;
    color: var(--tag-brown);
  }
  .now-price-label { left: 536px; top: 1430px; font-size: 78px; }
  .now-price {
    left: 536px;
    top: 1584px;
    font-size: 184px;
    color: var(--tag-brown);
  }
  .discount-rate {
    left: 250px;
    top: 1776px;
    font-size: 118px;
    color: var(--tag-green);
  }
  .discount-word {
    left: 254px;
    top: 1910px;
    font-size: 38px;
    color: var(--tag-green);
  }
  .was-price-label { left: 564px; top: 1936px; font-size: 78px; }
  .was-price {
    left: 548px;
    top: 2058px;
    font-size: 104px;
    color: var(--tag-brown);
  }
</style>
</head>
<body>
<main class="price-tag">
  <svg class="tag-frame" width="1200" height="2308" viewBox="0 0 1200 2308" aria-hidden="true">
    <rect class="outer-border" x="10" y="10" width="1180" height="2288" fill="none" stroke="var(--tag-green)" stroke-width="14"/>
    <rect class="inner-border" x="48" y="48" width="1104" height="2220" rx="120" ry="120" fill="none" stroke="var(--tag-brown)" stroke-width="7"/>
    <g class="field-boxes" fill="none" stroke="var(--tag-green)" stroke-width="5">
      <path class="box-store" d="M420 48 H1148 V352 A272 272 0 0 0 876 608 H420 Z"/>
      <path class="box-title" d="M420 640 H876 A272 272 0 0 0 1148 896 V1112 H420 Z"/>
      <rect class="box-product" x="420" y="1148" width="728" height="224"/>
      <path class="box-now" d="M420 1404 H1148 V1880 H550 A250 250 0 0 0 420 1677 Z"/>
      <path class="box-was" d="M550 1908 H1148 V2240 H420 V2115 A250 250 0 0 0 550 1908 Z"/>
    </g>
  </svg>

  <h1 class="tag-text store-name">Allied<br>Furniture<br>Depot</h1>
  <p class="tag-text new-flag">NEW!!</p>

  <p class="tag-text field-label item-title-label">Item Title</p>
  <p class="tag-text item-title">Black<br>King Bed</p>

  <p class="tag-text field-label product-number-label">Product Number</p>
  <p class="tag-text product-number">B9999</p>

  <p class="tag-text field-label now-price-label">Now Price</p>
  <p class="tag-text now-price">$555</p>

  <p class="tag-text discount-rate">25%</p>
  <p class="tag-text discount-word">DISCOUNT</p>

  <p class="tag-text field-label was-price-label">Was Price</p>
  <p class="tag-text was-price">$666</p>
</main>
</body>
</html>
```